Business Intelligence / Data Visualization Firm Seeking World Class Power Point Deck

Kestrel Arc delivers enterprise business intelligence and data visualization solutions enabling clients to see their business as they've never seen it - we transform complex, unstructured data into simple insight that facilitates intelligent decision making, revenue growth and risk reduction. We're seeking a world class power point template for internal, client and conference presentations.

Please visit kestrelarc.net for more company context.
*Note: A website photo has been uploaded and may be used or not used - designer discretion.

Additional context:
We use Quillmark: https://quillmark.brenvoda.com/products/predictive-analytics.

Target Market(s)

CXOs at Merivale 100 companies | small and medium business owners (BI / data-viz experts and also decision makers who don't actually understand BI / data-viz).

Industry/Entity Type

Professional Service

Font styles to use
Sans Serif
Other font styles liked:
• Our logo is Expansiva (uploaded), our site is Tahoma. Please use your discretion,.

Colors
ec1f27
ffffff
000000

Requirements
Must have
• PPT format, editable.
• Prefer simple, clean, strong presentation.
Nice to have
• Designs that relate to data, analytics, solutions, automation and transforming complexity into simplicity.
• Reusable icons.

```html
<!DOCTYPE html>
<html lang="en">
<head>
<meta charset="utf-8">
<title>Kestrel Arc – Individual Slides</title>
<link rel="stylesheet" href="https://fonts.googleapis.com/css2?family=Alfa+Slab+One&family=Michroma&family=Montserrat:wght@600;700;800&family=Open+Sans:wght@400;600;700&display=swap">
<style>
:root{
  --red:#ec1f27;
  --red-deep:#c8151c;
  --black:#000000;
  --ink:#1a1a1a;
  --char:#222326;
  --grey:#6b6b6b;
  --soft:#9a9a9a;
  --white:#ffffff;
  --page:#e4e1dc;
  --heading:#575757;
}
*{box-sizing:border-box;margin:0;padding:0}
html,body{width:1200px;height:1200px;overflow:hidden}
body{background:var(--page);font-family:"Open Sans",Tahoma,sans-serif;color:var(--ink);position:relative}
.sheet-title{position:absolute;top:12px;left:0;width:1200px;text-align:center;font-family:"Alfa Slab One",serif;font-size:24px;color:var(--heading);letter-spacing:.3px}
.deck{position:absolute;top:72px;left:131px;display:grid;grid-template-columns:repeat(3,286px);grid-auto-rows:162px;column-gap:48px;row-gap:27px}
.slide{position:relative;width:286px;height:162px;overflow:hidden;background:var(--white);box-shadow:0 3px 8px rgba(0,0,0,.28)}
.slide.dark{background:#111}
.abs{position:absolute}
.photo{position:absolute}
.ph-office{background:linear-gradient(135deg,#3d4046 0%,#25272b 45%,#181a1d 100%)}
.ph-desk{background:linear-gradient(160deg,#4a4d52 0%,#2c2e32 55%,#1c1d20 100%)}
.ph-meeting{background:linear-gradient(120deg,#34373c 0%,#222428 60%,#151618 100%)}
.ph-light{background:linear-gradient(135deg,#d9dde2 0%,#b4bac2 55%,#8d939b 100%)}
.ph-warm{background:linear-gradient(135deg,#e8e2d8 0%,#c9bca8 55%,#9e9282 100%)}
.ph-hand{background:linear-gradient(160deg,#8a96a6 0%,#56606d 55%,#2f353d 100%)}
.veil{position:absolute;inset:0;background:rgba(0,0,0,.45)}
.fill{position:absolute;inset:0;width:100%;height:100%}

/* company name, set in the deck's text font */
.brand-name{font-family:"Montserrat",sans-serif;font-weight:700;color:var(--white);white-space:nowrap;text-align:center}
.brand-name.on-white{color:var(--black)}
.brand-block{position:absolute;left:0;width:100%;text-align:center}

.pres-title{position:absolute;left:0;width:100%;text-align:center;font-family:"Montserrat",sans-serif;font-weight:800;color:var(--white);font-size:11.5px;letter-spacing:.2px}
.pres-sub{position:absolute;left:0;width:100%;text-align:center;font-size:3.4px;line-height:5px;color:#d8d8d8;font-style:italic}

.hd-bar{position:absolute;left:0;top:5px;width:3px;height:14px;background:var(--red)}
.hd-title{position:absolute;left:8px;top:6px;font-family:"Michroma",sans-serif;font-size:7.4px;color:var(--black);letter-spacing:.4px;white-space:nowrap}
.hd-sub{position:absolute;left:8px;top:15.5px;font-size:2.8px;color:var(--grey)}
.mini-name{position:absolute;right:7px;top:6px;font-family:"Montserrat",sans-serif;font-weight:700;font-size:5.4px;color:var(--black);white-space:nowrap}
.mini-name.light{color:var(--white)}
.foot{position:absolute;left:0;bottom:0;width:100%;height:5px;background:var(--black);display:flex;align-items:center;justify-content:space-between;padding:0 8px}
.foot span{font-family:"Open Sans",sans-serif;font-size:2.8px;color:var(--white);letter-spacing:.6px}

.para{position:absolute;font-size:3.1px;line-height:4.6px;color:var(--grey);font-style:italic}
.col{position:absolute;font-size:3px;line-height:4.4px;color:var(--grey);text-align:justify}
.col p+p{margin-top:3px}

.item{position:absolute;display:flex;gap:4px;align-items:flex-start;width:80px}
.item .t{font-family:"Montserrat",sans-serif;font-weight:600;font-size:4px;color:var(--ink);margin-top:1px}
.item .d{font-size:2.8px;line-height:4px;color:var(--grey)}

.num{flex:none;width:14px;height:14px;border-radius:50%;display:flex;align-items:center;justify-content:center;font-family:"Montserrat",sans-serif;font-weight:700;font-size:4px;color:var(--white);background:var(--red);box-shadow:0 0 0 1.5px #f6c7c9}
.num.blk{background:var(--black);box-shadow:0 0 0 1.5px #cfcfcf}
.ico{flex:none;width:14px;height:14px;border-radius:50%;background:var(--red);display:flex;align-items:center;justify-content:center;box-shadow:0 0 0 1.5px #f6c7c9}
.ico svg{width:8px;height:8px}
.ico.blk{background:var(--black);box-shadow:0 0 0 1.5px #cfcfcf}

.red-box{position:absolute;background:var(--red);color:var(--white)}
.red-box .bt{font-family:"Montserrat",sans-serif;font-weight:700;font-size:3.6px;text-align:center;margin:8px 0 4px}
.red-box p{font-size:2.9px;line-height:4.2px;padding:0 6px;color:#fde3e4}
.red-box p+p{margin-top:4px}

.diamond{position:absolute;width:30px;height:30px;transform:rotate(45deg);border:1.5px solid #fff;box-shadow:0 1px 3px rgba(0,0,0,.35)}
.member{position:absolute;width:50px;text-align:center}
.member .bars{display:flex;justify-content:center;gap:1px;margin-bottom:4px}
.member .bars i{display:block;width:2px;height:1.6px;background:#2b3bb0}
.member .n{font-size:3.2px;color:var(--ink);font-weight:600}
.member .r{font-size:2.6px;color:var(--soft)}

.step{position:absolute;width:36px;text-align:center;color:var(--white)}
.step .c{width:12px;height:12px;margin:0 auto;border-radius:50%;background:var(--white);color:var(--red);font-family:"Montserrat",sans-serif;font-weight:700;font-size:3.6px;display:flex;align-items:center;justify-content:center;box-shadow:0 0 0 2px rgba(255,255,255,.35)}
.step .t{font-family:"Montserrat",sans-serif;font-weight:700;font-size:3.6px;margin-top:8px}
.step .d{font-size:2.6px;line-height:3.6px;color:#fbd7d8}

.tl{position:absolute;left:143px;width:130px}
.tl .t{font-size:3.4px;font-weight:600;color:var(--ink)}
.tl .d{font-size:2.6px;line-height:3.6px;color:var(--grey)}
.tl-dot{position:absolute;left:135px;width:5px;height:5px;border-radius:50%;border:1.2px solid var(--red);background:#fff}
.hex-label{position:absolute;text-align:center}
.hex-label .a{font-size:3.2px;font-weight:600}
.hex-label .b{font-size:2.6px;color:var(--grey)}
</style>
</head>
<body>

<svg width="0" height="0" style="position:absolute" aria-hidden="true">
  <defs>
    <symbol id="i-bars" viewBox="0 0 10 10"><rect x="1" y="5" width="2" height="4" fill="#fff"/><rect x="4" y="2" width="2" height="7" fill="#fff"/><rect x="7" y="4" width="2" height="5" fill="#fff"/></symbol>
    <symbol id="i-search" viewBox="0 0 10 10"><circle cx="4.2" cy="4.2" r="2.8" fill="none" stroke="#fff" stroke-width="1.3"/><line x1="6.3" y1="6.3" x2="9" y2="9" stroke="#fff" stroke-width="1.5"/></symbol>
    <symbol id="i-pie" viewBox="0 0 10 10"><circle cx="5" cy="5" r="3.8" fill="none" stroke="#fff" stroke-width="1.2"/><path d="M5 5 V1.2 A3.8 3.8 0 0 1 8.8 5 Z" fill="#fff"/></symbol>
    <symbol id="i-stack" viewBox="0 0 10 10"><ellipse cx="5" cy="2.5" rx="3.5" ry="1.3" fill="#fff"/><path d="M1.5 4.5 Q5 6.6 8.5 4.5 M1.5 6.5 Q5 8.6 8.5 6.5" fill="none" stroke="#fff" stroke-width="1"/></symbol>
    <symbol id="i-gear" viewBox="0 0 10 10"><circle cx="5" cy="5" r="2.6" fill="none" stroke="#fff" stroke-width="1.6" stroke-dasharray="1.4 .7"/><circle cx="5" cy="5" r="1" fill="#fff"/></symbol>
    <symbol id="i-screen" viewBox="0 0 10 10"><rect x="1" y="1.8" width="8" height="5.4" rx=".6" fill="none" stroke="#fff" stroke-width="1.1"/><rect x="3.5" y="8" width="3" height="1" fill="#fff"/></symbol>
    <symbol id="i-trend" viewBox="0 0 10 10"><polyline points="1,8 4,5 6,6.5 9,2.5" fill="none" stroke="#fff" stroke-width="1.3"/><polyline points="6.8,2.5 9,2.5 9,4.7" fill="none" stroke="#fff" stroke-width="1.1"/></symbol>
  </defs>
</svg>

<h1 class="sheet-title">01 a - Individual Slides</h1>

<main class="deck">

  <!-- 1 cover: diagonal accents -->
  <section class="slide dark">
    <div class="photo ph-office fill" role="img" aria-label="Dim office photo of a team planning at a wall of notes"></div>
    <div class="veil"></div>
    <svg class="fill" viewBox="0 0 286 162" aria-hidden="true">
      <line x1="2" y1="6" x2="64" y2="58" stroke="#fff" stroke-width="1"/>
      <line x1="8" y1="4" x2="68" y2="54" stroke="#ec1f27" stroke-width="1"/>
      <line x1="218" y1="112" x2="280" y2="150" stroke="#ec1f27" stroke-width="1"/>
      <line x1="222" y1="108" x2="284" y2="146" stroke="#fff" stroke-width="1"/>
    </svg>
    <div class="brand-block" style="top:70px"><div class="brand-name" style="font-size:16px">Kestrel Arc</div></div>
  </section>

  <!-- 2 cover: dashed rules -->
  <section class="slide dark">
    <div class="photo ph-meeting fill" role="img" aria-label="Dim photo of colleagues meeting around a laptop"></div>
    <div class="veil"></div>
    <svg class="fill" viewBox="0 0 286 162" aria-hidden="true">
      <line x1="58" y1="54" x2="228" y2="54" stroke="#ec1f27" stroke-width="1.2" stroke-dasharray="6 3"/>
      <line x1="58" y1="103" x2="228" y2="103" stroke="#ec1f27" stroke-width="1.2" stroke-dasharray="6 3"/>
    </svg>
    <div class="brand-block" style="top:70px"><div class="brand-name" style="font-size:16px">Kestrel Arc</div></div>
  </section>

  <!-- 3 cover: title -->
  <section class="slide dark">
    <div class="photo ph-desk fill" role="img" aria-label="Dim photo of analysts working at their desks"></div>
    <div class="veil"></div>
    <div class="brand-block" style="top:40px"><div class="brand-name" style="font-size:17px">Kestrel Arc</div></div>
    <div class="pres-title" style="top:104px">PRESENTATION TITLE</div>
    <div class="pres-sub" style="top:122px">Clear data turns complex questions into simple answers for every leader.<br>One view of the business, built for faster and smarter decisions.</div>
  </section>

  <!-- 4 title over black band -->
  <section class="slide dark">
    <div class="photo ph-desk" style="left:0;top:0;width:286px;height:108px" role="img" aria-label="Dim photo of a team reviewing reports"></div>
    <div class="veil" style="height:108px"></div>
    <div class="pres-title" style="top:40px">PRESENTATION TITLE</div>
    <div class="pres-sub" style="top:58px">Clear data turns complex questions into simple answers for every leader.<br>One view of the business, built for faster and smarter decisions.</div>
    <div class="abs" style="left:0;top:108px;width:286px;height:54px;background:var(--black)"></div>
    <div class="brand-block" style="top:124px"><div class="brand-name" style="font-size:17px">Kestrel Arc</div></div>
  </section>

  <!-- 5 title over white band -->
  <section class="slide dark">
    <div class="photo ph-office" style="left:0;top:0;width:286px;height:108px" role="img" aria-label="Dim photo of a laptop on a desk"></div>
    <div class="veil" style="height:108px"></div>
    <div class="pres-title" style="top:40px">PRESENTATION TITLE</div>
    <div class="pres-sub" style="top:58px">Clear data turns complex questions into simple answers for every leader.<br>One view of the business, built for faster and smarter decisions.</div>
    <div class="abs" style="left:0;top:108px;width:286px;height:54px;background:var(--white)"></div>
    <div class="brand-block" style="top:124px"><div class="brand-name on-white" style="font-size:17px">Kestrel Arc</div></div>
  </section>

  <!-- 6 introduction -->
  <section class="slide">
    <div class="photo ph-meeting" style="left:0;top:0;width:114px;height:162px" role="img" aria-label="Dark photo of a server room"></div>
    <div class="veil" style="width:114px"></div>
    <div class="abs" style="left:0;top:64px;width:114px;text-align:center;font-family:'Michroma',sans-serif;font-size:8.4px;color:#fff;letter-spacing:.3px">INTRODUCTION</div>
    <div class="abs" style="left:0;top:77px;width:114px;text-align:center;font-size:3px;color:#ddd">Enter Your Subtitle Here</div>
    <div class="mini-name">Kestrel Arc</div>
    <svg class="abs" style="left:137px;top:24px" width="2" height="80" aria-hidden="true"><line x1="1" y1="0" x2="1" y2="80" stroke="#ec1f27" stroke-width=".8" stroke-dasharray="1.5 1.5"/></svg>
    <span class="tl-dot" style="top:24px;border-color:#2b3bb0"></span>
    <div class="tl" style="top:23px"><div class="t">Title 1</div><div class="d">Plain dashboards show what matters most and where to act next.</div></div>
    <span class="tl-dot" style="top:45px;border-color:#e98a16"></span>
    <div class="tl" style="top:44px"><div class="t">Title 2</div><div class="d">Plain dashboards show what matters most and where to act next.</div></div>
    <span class="tl-dot" style="top:66px;border-color:#777"></span>
    <div class="tl" style="top:65px"><div class="t">Title 3</div><div class="d">Plain dashboards show what matters most and where to act next.</div></div>
    <span class="tl-dot" style="top:87px;border-color:#e9c016"></span>
    <div class="tl" style="top:86px"><div class="t">Title 4</div><div class="d">Plain dashboards show what matters most and where to act next.</div></div>
    <div class="red-box" style="left:114px;top:106px;width:172px;height:51px">
      <p style="padding:6px 12px 0 16px;text-align:center">We turn scattered, unstructured data into one clear picture of the business, so teams can grow revenue, cut risk and decide with confidence. Every report is simple, current and ready to share.</p>
    </div>
    <svg class="abs" style="left:106px;top:123px" width="16" height="16" aria-hidden="true"><circle cx="8" cy="8" r="7.5" fill="#3a3e45"/><circle cx="8" cy="8" r="5.2" fill="none" stroke="#fff" stroke-width=".6"/><polyline points="7,5.5 9.5,8 7,10.5" fill="none" stroke="#fff" stroke-width=".9"/></svg>
    <div class="foot" style="left:114px;width:172px"><span>www.kestrelarc.net</span></div>
  </section>

  <!-- 7 agenda -->
  <section class="slide">
    <span class="hd-bar"></span><div class="hd-title">OUR AGENDA</div><div class="hd-sub">Enter your subtitle here</div>
    <div class="mini-name">Kestrel Arc</div>
    <div class="para" style="left:18px;top:24px;width:250px">Clear data turns complex questions into simple answers for every leader in the room. One trusted view of the business helps teams act faster and plan with confidence.</div>
    <div class="item" style="left:24px;top:52px"><span class="num">01</span><div><div class="t">Your Title Here</div><div class="d">Short note on this topic.</div></div></div>
    <div class="item" style="left:106px;top:52px"><span class="num blk">02</span><div><div class="t">Your Title Here</div><div class="d">Short note on this topic.</div></div></div>
    <div class="item" style="left:186px;top:52px"><span class="num">03</span><div><div class="t">Your Title Here</div><div class="d">Short note on this topic.</div></div></div>
    <div class="item" style="left:24px;top:86px"><span class="num blk">04</span><div><div class="t">Your Title Here</div><div class="d">Short note on this topic.</div></div></div>
    <div class="item" style="left:106px;top:86px"><span class="num">05</span><div><div class="t">Your Title Here</div><div class="d">Short note on this topic.</div></div></div>
    <div class="item" style="left:186px;top:86px"><span class="num blk">06</span><div><div class="t">Your Title Here</div><div class="d">Short note on this topic.</div></div></div>
    <div class="item" style="left:24px;top:118px"><span class="num">07</span><div><div class="t">Your Title Here</div><div class="d">Short note on this topic.</div></div></div>
    <div class="item" style="left:106px;top:118px"><span class="num blk">08</span><div><div class="t">Your Title Here</div><div class="d">Short note on this topic.</div></div></div>
    <div class="item" style="left:186px;top:118px"><span class="num">09</span><div><div class="t">Your Title Here</div><div class="d">Short note on this topic.</div></div></div>
    <div class="foot"><span>www.kestrelarc.net</span><span>07</span></div>
  </section>

  <!-- 8 title + red box + icons -->
  <section class="slide">
    <span class="hd-bar"></span><div class="hd-title">YOUR TITLE HERE</div><div class="hd-sub">Enter your subtitle here</div>
    <div class="mini-name">Kestrel Arc</div>
    <div class="para" style="left:18px;top:28px;width:250px">Clear data turns complex questions into simple answers for every leader in the room. One trusted view of the business helps teams act faster, plan with confidence and share results across the company.</div>
    <div class="red-box" style="left:18px;top:57px;width:86px;height:76px">
      <div class="bt">TITLE GOES HERE</div>
      <p>Live reports replace manual exports, so numbers stay current and easy to trust.</p>
      <p>Every chart links back to its source, giving teams one shared version of the facts.</p>
    </div>
    <div class="item" style="left:116px;top:64px"><span class="ico"><svg><use href="#i-pie"/></svg></span><div><div class="t">Title Goes Here</div><div class="d">Fits any business topic.</div></div></div>
    <div class="item" style="left:198px;top:64px"><span class="ico"><svg><use href="#i-trend"/></svg></span><div><div class="t">Title Goes Here</div><div class="d">Fits any business topic.</div></div></div>
    <div class="item" style="left:116px;top:100px"><span class="ico"><svg><use href="#i-bars"/></svg></span><div><div class="t">Title Goes Here</div><div class="d">Fits any business topic.</div></div></div>
    <div class="item" style="left:198px;top:100px"><span class="ico"><svg><use href="#i-search"/></svg></span><div><div class="t">Title Goes Here</div><div class="d">Fits any business topic.</div></div></div>
    <div class="foot"><span>www.kestrelarc.net</span><span>08</span></div>
  </section>

  <!-- 9 one column -->
  <section class="slide">
    <span class="hd-bar"></span><div class="hd-title">ONE CLOUMN</div><div class="hd-sub">Enter your subtitle here</div>
    <div class="mini-name">Kestrel Arc</div>
    <div class="col" style="left:22px;top:32px;width:242px">
      <p>Clear data turns complex questions into simple answers. We connect sales, finance and operations into one model, so every leader reads the same numbers and trusts what they see on screen.</p>
      <p>Dashboards refresh on their own, alerts point to change early, and each chart explains itself in plain words for people who do not live in spreadsheets.</p>
      <p>From first workshop to live rollout, our team maps the questions that matter, cleans the data behind them and builds views that guide real decisions every week. The result is less time hunting for figures and more time acting on them.</p>
      <p>Simple insight, shared widely, helps grow revenue and lower risk.</p>
    </div>
    <div class="foot"><span>www.kestrelarc.net</span><span>09</span></div>
  </section>

  <!-- 10 two columns -->
  <section class="slide">
    <span class="hd-bar"></span><div class="hd-title">TWO CLOUMNS</div><div class="hd-sub">Enter your subtitle here</div>
    <div class="mini-name">Kestrel Arc</div>
    <div class="col" style="left:22px;top:34px;width:112px">
      <p>Clear data turns complex questions into simple answers. We link every source into one model so leaders read the same numbers.</p>
      <p>Dashboards refresh on their own and alerts point to change early, in plain words.</p>
      <p>Our team maps the questions that matter and builds views that guide real decisions every week.</p>
    </div>
    <div class="col" style="left:152px;top:34px;width:112px">
      <p>Live reports replace manual exports, so figures stay current and easy to trust across teams.</p>
      <p>Each chart links back to its source, giving one shared version of the facts.</p>
      <p>Less time hunting for figures means more time acting on them, growing revenue and lowering risk.</p>
    </div>
    <div class="foot"><span>www.kestrelarc.net</span><span>10</span></div>
  </section>

  <!-- 11 three columns -->
  <section class="slide">
    <span class="hd-bar"></span><div class="hd-title">THREE CLOUMNS</div><div class="hd-sub">Enter your subtitle here</div>
    <div class="mini-name">Kestrel Arc</div>
    <div class="col" style="left:22px;top:32px;width:74px">
      <p>Clear data turns complex questions into simple answers for every leader.</p>
      <p>We link every source into one model so teams read the same numbers.</p>
      <p>Dashboards refresh on their own and flag change early.</p>
    </div>
    <div class="col" style="left:106px;top:32px;width:74px">
      <p>Live reports replace manual exports and stay current.</p>
      <p>Each chart links back to its source for one shared set of facts.</p>
      <p>Alerts explain themselves in plain words for every reader.</p>
    </div>
    <div class="col" style="left:190px;top:32px;width:74px">
      <p>Our team maps the questions that matter most.</p>
      <p>We clean the data behind them and build views that guide decisions.</p>
      <p>Less hunting for figures, more time acting on them.</p>
    </div>
    <div class="foot"><span>www.kestrelarc.net</span><span>11</span></div>
  </section>

  <!-- 12 process band -->
  <section class="slide">
    <span class="hd-bar"></span><div class="hd-title">YOUR TITLE HERE</div><div class="hd-sub">Enter your subtitle here</div>
    <div class="mini-name">Kestrel Arc</div>
    <div class="para" style="left:18px;top:27px;width:250px">Clear data turns complex questions into simple answers for every leader in the room. One trusted view helps teams act faster and plan with confidence.</div>
    <div class="abs" style="left:0;top:53px;width:286px;height:75px;background:linear-gradient(180deg,#ec1f27,#c8151c)"></div>
    <svg class="abs" style="left:0;top:53px" width="286" height="75" aria-hidden="true"><line x1="28" y1="18" x2="258" y2="18" stroke="#fff" stroke-width=".6" stroke-dasharray="1.5 1.5"/></svg>
    <div class="step" style="left:10px;top:65px"><div class="c">01</div><div class="t">Your Title</div><div class="d">Short note here</div></div>
    <div class="step" style="left:55px;top:65px"><div class="c">02</div><div class="t">Your Title</div><div class="d">Short note here</div></div>
    <div class="step" style="left:100px;top:65px"><div class="c">03</div><div class="t">Your Title</div><div class="d">Short note here</div></div>
    <div class="step" style="left:146px;top:65px"><div class="c">04</div><div class="t">Your Title</div><div class="d">Short note here</div></div>
    <div class="step" style="left:192px;top:65px"><div class="c">05</div><div class="t">Your Title</div><div class="d">Short note here</div></div>
    <div class="step" style="left:238px;top:65px"><div class="c">06</div><div class="t">Your Title</div><div class="d">Short note here</div></div>
    <div class="foot"><span>www.kestrelarc.net</span><span>12</span></div>
  </section>

  <!-- 13 image + icons -->
  <section class="slide">
    <span class="hd-bar"></span><div class="hd-title">YOUR TITLE HERE</div><div class="hd-sub">Enter your subtitle here</div>
    <div class="mini-name">Kestrel Arc</div>
    <div class="para" style="left:18px;top:27px;width:250px">Clear data turns complex questions into simple answers for every leader in the room. One trusted view of the business helps teams act faster, plan with confidence and share results.</div>
    <div class="photo ph-light" style="left:17px;top:55px;width:86px;height:64px" role="img" aria-label="Photo of a hand signing a document beside a coffee cup"></div>
    <div class="item" style="left:114px;top:66px"><span class="ico"><svg><use href="#i-stack"/></svg></span><div><div class="t">Title Goes Here</div><div class="d">Fits any business topic.</div></div></div>
    <div class="item" style="left:196px;top:66px"><span class="ico"><svg><use href="#i-stack"/></svg></span><div><div class="t">Title Goes Here</div><div class="d">Fits any business topic.</div></div></div>
    <div class="item" style="left:114px;top:102px"><span class="ico"><svg><use href="#i-bars"/></svg></span><div><div class="t">Title Goes Here</div><div class="d">Fits any business topic.</div></div></div>
    <div class="item" style="left:196px;top:102px"><span class="ico"><svg><use href="#i-bars"/></svg></span><div><div class="t">Title Goes Here</div><div class="d">Fits any business topic.</div></div></div>
    <div class="foot"><span>www.kestrelarc.net</span><span>13</span></div>
  </section>

  <!-- 14 team -->
  <section class="slide">
    <span class="hd-bar"></span><div class="hd-title">OUR TEAM</div>
    <div class="mini-name">Kestrel Arc</div>
    <div class="para" style="left:18px;top:23px;width:250px">Clear data turns complex questions into simple answers for every leader in the room. One trusted view helps teams act faster.</div>
    <div class="diamond ph-meeting" style="left:29px;top:55px" role="img" aria-label="Team member portrait"></div>
    <div class="diamond ph-light" style="left:92px;top:55px" role="img" aria-label="Team member portrait"></div>
    <div class="diamond ph-light" style="left:159px;top:55px" role="img" aria-label="Team member portrait"></div>
    <div class="diamond ph-warm" style="left:221px;top:55px" role="img" aria-label="Team member portrait"></div>
    <div class="member" style="left:19px;top:111px"><div class="bars"><i></i><i></i><i></i><i></i><i></i></div><div class="n">Enter Name</div><div class="r">Designation</div></div>
    <div class="member" style="left:82px;top:111px"><div class="bars"><i></i><i></i><i></i><i></i><i></i></div><div class="n">Enter Name</div><div class="r">Designation</div></div>
    <div class="member" style="left:149px;top:111px"><div class="bars"><i></i><i></i><i></i><i></i><i></i></div><div class="n">Enter Name</div><div class="r">Designation</div></div>
    <div class="member" style="left:211px;top:111px"><div class="bars"><i></i><i></i><i></i><i></i><i></i></div><div class="n">Enter Name</div><div class="r">Designation</div></div>
    <div class="foot"><span>www.kestrelarc.net</span><span>14</span></div>
  </section>

  <!-- 15 dark side + numbered -->
  <section class="slide">
    <div class="photo ph-desk" style="left:0;top:0;width:114px;height:162px" role="img" aria-label="Dark photo of a workspace"></div>
    <div class="veil" style="width:114px;background:rgba(0,0,0,.55)"></div>
    <div class="abs" style="left:14px;top:28px;width:88px;font-size:3.2px;line-height:5px;color:#eee;text-align:center">Clear data turns complex questions into simple answers for every leader. One trusted view of the business helps teams act faster and plan with confidence.<br><br>Live reports replace manual exports, so figures stay current. Each chart links back to its source, giving one shared version of the facts for every team.</div>
    <div class="hd-title" style="left:118px">YOUR TITLE HERE</div><div class="hd-sub" style="left:118px">Enter your subtitle here</div>
    <div class="mini-name">Kestrel Arc</div>
    <div class="para" style="left:124px;top:28px;width:150px">Clear data turns complex questions into simple answers for every leader. One trusted view helps teams act faster and plan with confidence.</div>
    <div class="item" style="left:122px;top:78px"><span class="num">01</span><div><div class="t">Title Goes Here</div><div class="d">Fits any business topic.</div></div></div>
    <div class="item" style="left:204px;top:78px"><span class="num">02</span><div><div class="t">Title Goes Here</div><div class="d">Fits any business topic.</div></div></div>
    <div class="item" style="left:122px;top:114px"><span class="num">03</span><div><div class="t">Title Goes Here</div><div class="d">Fits any business topic.</div></div></div>
    <div class="item" style="left:204px;top:114px"><span class="num">04</span><div><div class="t">Title Goes Here</div><div class="d">Fits any business topic.</div></div></div>
    <div class="foot" style="left:114px;width:172px"><span>www.kestrelarc.net</span><span>15</span></div>
  </section>

  <!-- 16 red/black split -->
  <section class="slide">
    <div class="abs" style="left:0;top:0;width:72px;height:162px;background:var(--red)"></div>
    <div class="abs" style="left:72px;top:0;width:70px;height:162px;background:var(--char)"></div>
    <div class="abs" style="left:8px;top:7px;font-family:'Michroma',sans-serif;font-size:9px;color:#fff;white-space:nowrap;letter-spacing:.3px">YOUR TITLE HERE</div>
    <div class="step" style="left:18px;top:32px"><div class="c">01</div><div class="t" style="margin-top:5px">TITLE GOES HERE</div><div class="d" style="color:#fde3e4">Short note about this point here</div></div>
    <div class="step" style="left:89px;top:32px"><div class="c" style="color:var(--black)">02</div><div class="t" style="margin-top:5px">TITLE GOES HERE</div><div class="d" style="color:#cfcfcf">Short note about this point here</div></div>
    <div class="step" style="left:18px;top:92px"><div class="c">03</div><div class="t" style="margin-top:5px">TITLE GOES HERE</div><div class="d" style="color:#fde3e4">Short note about this point here</div></div>
    <div class="step" style="left:89px;top:92px"><div class="c" style="color:var(--black)">04</div><div class="t" style="margin-top:5px">TITLE GOES HERE</div><div class="d" style="color:#cfcfcf">Short note about this point here</div></div>
    <div class="mini-name">Kestrel Arc</div>
    <div class="para" style="left:152px;top:26px;width:118px;font-style:normal">Clear data turns complex questions into simple answers for every leader. One trusted view helps teams act faster and plan with confidence.<br><br>Live reports replace manual exports, so figures stay current and easy to trust.</div>
    <div class="item" style="left:154px;top:95px;width:118px"><span class="ico blk" style="box-shadow:none"><svg><use href="#i-screen"/></svg></span><div><div class="d">Plain dashboards show what matters most and where to act.</div></div></div>
    <div class="item" style="left:154px;top:121px;width:118px"><span class="ico" style="box-shadow:none"><svg><use href="#i-screen"/></svg></span><div><div class="d">Plain dashboards show what matters most and where to act.</div></div></div>
    <div class="foot" style="left:142px;width:144px"><span>www.kestrelarc.net</span></div>
  </section>

  <!-- 17 dark top band + photo -->
  <section class="slide">
    <div class="photo ph-meeting" style="left:0;top:0;width:286px;height:52px" role="img" aria-label="Dark photo of a conference room"></div>
    <div class="veil" style="height:52px;background:rgba(0,0,0,.55)"></div>
    <div class="abs" style="left:0;top:8px;width:286px;text-align:center;font-family:'Michroma',sans-serif;font-size:9px;color:#fff;letter-spacing:.4px">YOUR TITLE HERE</div>
    <div class="mini-name light">Kestrel Arc</div>
    <div class="para" style="left:18px;top:24px;width:250px;color:#d5d5d5">Clear data turns complex questions into simple answers for every leader in the room. One trusted view of the business helps teams act faster, plan with confidence and share results across the company.</div>
    <div class="photo ph-light" style="left:16px;top:65px;width:110px;height:84px" role="img" aria-label="Photo of a team meeting in a bright office"></div>
    <div class="item" style="left:150px;top:66px;width:125px"><span class="ico" style="box-shadow:none"><svg><use href="#i-stack"/></svg></span><div><div class="t">Your Title Here</div><div class="d">Plain dashboards show what matters most and where to act next.</div></div></div>
    <div class="item" style="left:150px;top:95px;width:125px"><span class="ico" style="box-shadow:none"><svg><use href="#i-bars"/></svg></span><div><div class="t">Your Title Here</div><div class="d">Plain dashboards show what matters most and where to act next.</div></div></div>
    <div class="item" style="left:150px;top:124px;width:125px"><span class="ico" style="box-shadow:none"><svg><use href="#i-stack"/></svg></span><div><div class="t">Your Title Here</div><div class="d">Plain dashboards show what matters most and where to act next.</div></div></div>
    <div class="foot"><span>www.kestrelarc.net</span></div>
  </section>

  <!-- 18 hex cluster -->
  <section class="slide">
    <div class="photo ph-hand" style="left:0;top:0;width:79px;height:162px" role="img" aria-label="Photo of a hand writing notes on paper"></div>
    <div class="abs" style="left:8px;top:93px;width:64px;font-size:3.2px;line-height:5px;color:#fff;text-align:center">Clear data turns complex questions into simple answers. One trusted view of the business helps every team act faster and plan with confidence.</div>
    <div class="hd-title" style="left:84px;top:5px">YOUR TITLE HERE</div><div class="hd-sub" style="left:84px;top:14px">Enter your subtitle here</div>
    <div class="mini-name">Kestrel Arc</div>
    <div class="para" style="left:86px;top:26px;width:188px;font-style:normal">Clear data turns complex questions into simple answers for every leader. One trusted view helps teams act faster and plan with confidence.</div>
    <svg class="abs" style="left:144px;top:54px" width="92" height="94" viewBox="0 0 92 94" aria-hidden="true">
      <g stroke="#fff" stroke-width="1.2">
        <polygon points="33,4 46,11.5 46,26.5 33,34 20,26.5 20,11.5" fill="#ec1f27"/>
        <polygon points="59,4 72,11.5 72,26.5 59,34 46,26.5 46,11.5" fill="#000"/>
        <polygon points="20,27 33,34.5 33,49.5 20,57 7,49.5 7,34.5" fill="#000"/>
        <polygon points="46,27 59,34.5 59,49.5 46,57 33,49.5 33,34.5" fill="#fff" stroke="#ddd"/>
        <polygon points="72,27 85,34.5 85,49.5 72,57 59,49.5 59,34.5" fill="#ec1f27"/>
        <polygon points="33,50 46,57.5 46,72.5 33,80 20,72.5 20,57.5" fill="#ec1f27"/>
        <polygon points="59,50 72,57.5 72,72.5 59,80 46,72.5 46,57.5" fill="#000"/>
      </g>
      <use href="#i-bars" x="28" y="14" width="10" height="10"/>
      <use href="#i-gear" x="54" y="14" width="10" height="10"/>
      <use href="#i-stack" x="15" y="37" width="10" height="10"/>
      <use href="#i-pie" x="67" y="37" width="10" height="10"/>
      <use href="#i-screen" x="28" y="60" width="10" height="10"/>
      <use href="#i-trend" x="54" y="60" width="10" height="10"/>
    </svg>
    <div class="hex-label" style="left:84px;top:64px;width:58px"><div class="a">Title Goes Here</div><div class="b">Fits any business topic</div></div>
    <div class="hex-label" style="left:84px;top:86px;width:58px"><div class="a">Title Goes Here</div><div class="b">Fits any business topic</div></div>
    <div class="hex-label" style="left:84px;top:108px;width:58px"><div class="a">Title Goes Here</div><div class="b">Fits any business topic</div></div>
    <div class="hex-label" style="left:232px;top:64px;width:52px"><div class="a">Title Goes Here</div><div class="b">Fits any business topic</div></div>
    <div class="hex-label" style="left:232px;top:86px;width:52px"><div class="a">Title Goes Here</div><div class="b">Fits any business topic</div></div>
    <div class="hex-label" style="left:232px;top:108px;width:52px"><div class="a">Title Goes Here</div><div class="b">Fits any business topic</div></div>
    <div class="foot" style="left:79px;width:207px"><span>www.kestrelarc.net</span></div>
  </section>

</main>
</body>
</html>
```